Brain Risk Assessment

We need an illustration similar to the graphic attached that shows your brain performance lowers as you age. The goal of this is to show that if you make small changes earlier in life, it helps keep you sharp and prevents disease later on in life. If you change your brain health in your 40's and 50's, you made add 10 to 20 quality, brain healthy years to your life.

Target Market(s)

Consumer

Industry/Entity Type

Health

Font styles to use
Sans Serif

Colors
33a6d7
3276b5

Requirements
Must have
• Show multiple trajectories based on small improvements in brain health in 40's and 50's

```html
<!DOCTYPE html>
<html lang="en">
<head>
<meta charset="utf-8">
<title>Brain Performance Across the Lifespan</title>
<link rel="stylesheet" href="https://fonts.googleapis.com/css2?family=Montserrat:wght@600;700&display=swap">
<style>
  :root {
    --paper: #ffffff;
    --navy: #013263;
    --ink-dark: #0b3a6b;
    --ink-light: #ffffff;
    --axis: #5d9fe2;
    --baseline-curve: #6aa6e6;
    --improved-curve: #a9a9a9;
    --band-deep: #4f8fd8;
    --band-soft: #a8d2ff;
    --figure-dark: #2f74b8;
    --figure-light: #ffffff;
    --ground: #d6d6d6;
  }
  html, body {
    margin: 0;
    padding: 0;
    width: 1200px;
    height: 1000px;
    overflow: hidden;
    background: var(--paper);
  }
  .canvas { display: block; width: 1200px; height: 1000px; }
  .label {
    font-family: "Montserrat", sans-serif;
    font-weight: 700;
    font-size: 15px;
  }
  .age {
    font-family: "Montserrat", sans-serif;
    font-weight: 700;
    font-size: 16px;
    fill: var(--axis);
    text-anchor: middle;
  }
  .axis, .tick { stroke: var(--axis); stroke-width: 2; fill: none; }
  .curve { fill: none; stroke-width: 3; stroke-linecap: round; }
  .curve--baseline { stroke: var(--baseline-curve); }
  .curve--improved { stroke: var(--improved-curve); }
  .gain { stroke: var(--axis); stroke-width: 2; fill: none; }
  .gain-head { fill: var(--axis); }
  .ground { fill: var(--ground); }
  .chart--light .label { fill: var(--ink-dark); }
  .chart--light .figure { fill: var(--figure-dark); }
  .chart--dark .label { fill: var(--ink-light); }
  .chart--dark .figure { fill: var(--figure-light); }
  .chart--dark .ground { opacity: .8; }
</style>
</head>
<body>
<svg class="canvas" viewBox="0 0 1200 1000" xmlns="http://www.w3.org/2000/svg">
  <defs>
    <linearGradient id="band-rise" x1="0" y1="0" x2="0" y2="1">
      <stop offset="0" stop-color="#ffffff" stop-opacity="0"/>
      <stop offset="1" stop-color="#4f8fd8"/>
    </linearGradient>
    <linearGradient id="band-rise-soft" x1="0" y1="0" x2="0" y2="1">
      <stop offset="0" stop-color="#ffffff" stop-opacity="0"/>
      <stop offset="1" stop-color="#a8d2ff"/>
    </linearGradient>
    <linearGradient id="band-night" x1="0" y1="0" x2="0" y2="1">
      <stop offset="0" stop-color="#013263" stop-opacity="0"/>
      <stop offset="1" stop-color="#4f8fd8"/>
    </linearGradient>
    <linearGradient id="band-night-soft" x1="0" y1="0" x2="0" y2="1">
      <stop offset="0" stop-color="#013263" stop-opacity="0"/>
      <stop offset="1" stop-color="#a8d2ff"/>
    </linearGradient>
  </defs>

  <rect x="0" y="0" width="1200" height="547" fill="var(--paper)"/>
  <rect x="0" y="547" width="1200" height="453" fill="var(--navy)"/>

  <!-- Light chart -->
  <g class="chart chart--light">
    <rect x="241" y="222" width="48" height="210" fill="url(#band-rise)"/>
    <rect x="306" y="222" width="48" height="210" fill="url(#band-rise-soft)"/>
    <rect x="387" y="222" width="48" height="210" fill="url(#band-rise-soft)"/>
    <rect x="476" y="222" width="48" height="210" fill="url(#band-rise)"/>
    <rect x="571" y="222" width="48" height="210" fill="url(#band-rise)"/>
    <rect x="676" y="222" width="48" height="210" fill="url(#band-rise-soft)"/>
    <rect x="773" y="222" width="48" height="210" fill="url(#band-rise)"/>
    <rect x="873" y="222" width="48" height="210" fill="url(#band-rise)"/>

    <ellipse class="ground" cx="585" cy="431" rx="345" ry="5"/>

    <g role="img" aria-label="Silhouettes of one person at eight life stages, from crawling baby to older adult with a cane">
      <rect class="figure" x="246" y="392" width="40" height="38" rx="10"/>
      <rect class="figure" x="311" y="354" width="36" height="78" rx="10"/>
      <rect class="figure" x="389" y="322" width="42" height="110" rx="10"/>
      <rect class="figure" x="468" y="290" width="56" height="144" rx="10"/>
      <rect class="figure" x="558" y="282" width="70" height="150" rx="10"/>
      <rect class="figure" x="664" y="298" width="72" height="132" rx="12"/>
      <rect class="figure" x="766" y="310" width="72" height="122" rx="12"/>
      <rect class="figure" x="872" y="326" width="42" height="106" rx="10"/>
    </g>

    <path class="curve curve--improved" d="M213 372 Q600 117 948 275"/>
    <path class="curve curve--baseline" d="M213 380 Q520 160 955 347"/>

    <line class="gain" x1="595" y1="258" x2="595" y2="228"/>
    <path class="gain-head" d="M590 230 L595 221 L600 230 Z"/>
    <line class="gain" x1="700" y1="268" x2="700" y2="235"/>
    <path class="gain-head" d="M695 237 L700 228 L705 237 Z"/>
    <line class="gain" x1="797" y1="292" x2="797" y2="248"/>
    <line class="gain" x1="897" y1="322" x2="897" y2="266"/>
    <path class="gain-head" d="M892 268 L897 259 L902 268 Z"/>

    <line class="axis" x1="213" y1="447" x2="213" y2="180"/>
    <path class="gain-head" d="M206 186 L213 171 L220 186 Z"/>
    <line class="axis" x1="213" y1="447" x2="958" y2="447"/>
    <path class="gain-head" d="M953 440 L968 447 L953 454 Z"/>

    <g>
      <line class="tick" x1="267" y1="440" x2="267" y2="458"/>
      <line class="tick" x1="330" y1="440" x2="330" y2="458"/>
      <line class="tick" x1="412" y1="440" x2="412" y2="458"/>
      <line class="tick" x1="498" y1="440" x2="498" y2="458"/>
      <line class="tick" x1="595" y1="440" x2="595" y2="458"/>
      <line class="tick" x1="700" y1="440" x2="700" y2="458"/>
      <line class="tick" x1="797" y1="440" x2="797" y2="458"/>
      <line class="tick" x1="897" y1="440" x2="897" y2="458"/>
    </g>
    <text class="age" x="595" y="478">40</text>
    <text class="age" x="700" y="478">45</text>
    <text class="age" x="797" y="478">50</text>
    <text class="age" x="897" y="478">60</text>

    <text class="label" x="244" y="182">Improve</text>
    <text class="label" x="244" y="201">performance</text>
    <text class="label" x="888" y="182">Delay</text>
    <text class="label" x="888" y="201">disease</text>
  </g>

  <!-- Dark chart -->
  <g class="chart chart--dark" transform="translate(78.5 497.4) scale(0.885)">
    <rect x="241" y="222" width="48" height="210" fill="url(#band-night)"/>
    <rect x="306" y="222" width="48" height="210" fill="url(#band-night)"/>
    <rect x="387" y="222" width="48" height="210" fill="url(#band-night-soft)"/>
    <rect x="476" y="222" width="48" height="210" fill="url(#band-night-soft)"/>
    <rect x="571" y="222" width="48" height="210" fill="url(#band-night)"/>
    <rect x="676" y="222" width="48" height="210" fill="url(#band-night-soft)"/>
    <rect x="773" y="222" width="48" height="210" fill="url(#band-night)"/>
    <rect x="873" y="222" width="48" height="210" fill="url(#band-night)"/>

    <ellipse class="ground" cx="585" cy="431" rx="345" ry="5"/>

    <g role="img" aria-label="Silhouettes of one person at eight life stages, from crawling baby to older adult with a cane">
      <rect class="figure" x="246" y="392" width="40" height="38" rx="10"/>
      <rect class="figure" x="311" y="354" width="36" height="78" rx="10"/>
      <rect class="figure" x="389" y="322" width="42" height="110" rx="10"/>
      <rect class="figure" x="468" y="290" width="56" height="144" rx="10"/>
      <rect class="figure" x="558" y="282" width="70" height="150" rx="10"/>
      <rect class="figure" x="664" y="298" width="72" height="132" rx="12"/>
      <rect class="figure" x="766" y="310" width="72" height="122" rx="12"/>
      <rect class="figure" x="872" y="326" width="42" height="106" rx="10"/>
    </g>

    <path class="curve curve--improved" d="M213 372 Q600 117 948 275"/>
    <path class="curve curve--baseline" d="M213 380 Q520 160 955 347"/>

    <line class="gain" x1="595" y1="258" x2="595" y2="228"/>
    <path class="gain-head" d="M590 230 L595 221 L600 230 Z"/>
    <line class="gain" x1="700" y1="268" x2="700" y2="235"/>
    <path class="gain-head" d="M695 237 L700 228 L705 237 Z"/>
    <line class="gain" x1="797" y1="292" x2="797" y2="248"/>
    <path class="gain-head" d="M792 250 L797 241 L802 250 Z"/>
    <line class="gain" x1="897" y1="322" x2="897" y2="266"/>

    <line class="axis" x1="213" y1="447" x2="213" y2="180"/>
    <path class="gain-head" d="M206 186 L213 171 L220 186 Z"/>
    <line class="axis" x1="213" y1="447" x2="958" y2="447"/>
    <path class="gain-head" d="M953 440 L968 447 L953 454 Z"/>

    <g>
      <line class="tick" x1="267" y1="440" x2="267" y2="458"/>
      <line class="tick" x1="330" y1="440" x2="330" y2="458"/>
      <line class="tick" x1="412" y1="440" x2="412" y2="458"/>
      <line class="tick" x1="498" y1="440" x2="498" y2="458"/>
      <line class="tick" x1="595" y1="440" x2="595" y2="458"/>
      <line class="tick" x1="700" y1="440" x2="700" y2="458"/>
      <line class="tick" x1="797" y1="440" x2="797" y2="458"/>
      <line class="tick" x1="897" y1="440" x2="897" y2="458"/>
    </g>
    <text class="age" x="595" y="478">40</text>
    <text class="age" x="700" y="478">45</text>
    <text class="age" x="797" y="478">50</text>
    <text class="age" x="897" y="478">60</text>

    <text class="label" x="244" y="182" style="font-size:17px">Improve</text>
    <text class="label" x="244" y="203" style="font-size:17px">performance</text>
    <text class="label" x="872" y="182" style="font-size:17px">Delay</text>
    <text class="label" x="872" y="203" style="font-size:17px">disease</text>
  </g>
</svg>
</body>
</html>
```